Rosalind Vetteray Gymnastics Center Business Card

Develop a business card with my RV logo provided. A classy and unique design using the colors black, white, purple and maybe a splash of gold. Add Address (219 W. Lantern Ridge Road Medina, Ohio 44871), email (RosalindVetterayGymnasticsCtr@brellomail.com, website (www.RosalindVetterayGymnasticsCenter.example), phone number (216-555-0148) on the card. Social media if there's room also. t: @VetterayGym, i: @VetterayGym, f: @RosalindVetterayGymnasticsCenter

Target Market(s)

Families, children, gymnastics community and beyond

Industry/Entity Type

Business

Contact Information for Business Card

Add name (Rosalind Vetteray) who is the owner. Add logo, add address details, classy font, uniqueness important, rounded edges on business card. Horizontal business card needed.

Font styles to use
Serif
Sans Serif

Colors
6b449b
ffffff

Requirements
Must have
• Must have logo, owner name and owner on card, must have colors purple, white, black where needed in print, and a splash of gold if appropriate. Keep card classy and clean. Must have address of location, phone number, website of business, email and social media.
Nice to have
• I am open here, but I'd appreciate uniqueness. Must be a lasting image for branding...
Should not have
• No kid-like looks...

```html
<!DOCTYPE html>
<html lang="en">
<head>
<meta charset="utf-8">
<title>Rosalind Vetteray Gymnastics Center — Business Card</title>
<link rel="stylesheet" href="https://fonts.googleapis.com/css2?family=Lato:wght@400;700&family=Cormorant+Garamond:wght@500&display=swap">
<style>
  :root {
    --purple: #6b449b;
    --black: #000000;
    --white: #ffffff;
    --stage: #4a4a4a;
    --ghost: #eeecf4;
    --ink: #111111;
  }
  * { margin: 0; padding: 0; box-sizing: border-box; }
  html, body { width: 1189px; height: 1200px; overflow: hidden; }
  body {
    background: var(--stage);
    font-family: "Lato", Arial, sans-serif;
    position: relative;
  }
  .card {
    position: absolute;
    left: 171px;
    width: 856px;
    height: 488px;
    overflow: hidden;
  }
  .card--front {
    top: 67px;
    background: var(--black);
    color: var(--white);
    border-radius: 230px 24px 24px 24px;
  }
  .card--back {
    top: 626px;
    background: var(--white);
    color: var(--ink);
    border-radius: 24px 230px 24px 24px;
  }

  /* brand lockup */
  .brand {
    position: absolute;
    display: flex;
    flex-direction: column;
    align-items: center;
    text-align: center;
  }
  .card--front .brand { right: 42px; top: 52px; width: 300px; }
  .card--back .brand { left: 0; right: 0; top: 142px; }
  .brand__mark {
    display: block;
    background: var(--purple);
  }
  .card--front .brand__mark { width: 104px; height: 104px; margin-bottom: 16px; }
  .card--back .brand__mark { width: 116px; height: 116px; margin-bottom: 12px; }
  .brand__name {
    font-weight: 700;
    font-variant: small-caps;
    letter-spacing: 1px;
    line-height: 1.02;
  }
  .card--front .brand__name { font-size: 27px; color: var(--white); }
  .card--back .brand__name { font-size: 30px; color: var(--black); }
  .brand__tagline {
    font-family: "Cormorant Garamond", "Times New Roman", serif;
    font-weight: 500;
    color: var(--purple);
    border-top: 1px solid var(--purple);
    padding-top: 1px;
    letter-spacing: 0.3px;
  }
  .card--front .brand__tagline { font-size: 19px; margin-top: 3px; width: 268px; }
  .card--back .brand__tagline { font-size: 21px; margin-top: 4px; width: 296px; }

  /* owner */
  .owner-tab {
    position: absolute;
    left: -18px;
    top: 243px;
    width: 36px;
    height: 36px;
    border-radius: 50%;
    background: var(--purple);
  }
  .owner {
    position: absolute;
    left: 31px;
    top: 236px;
  }
  .owner__name { font-size: 27px; font-weight: 700; line-height: 1.05; }
  .owner__title { font-size: 21px; color: var(--purple); line-height: 1; }

  /* contact */
  .contact {
    position: absolute;
    left: 33px;
    top: 304px;
    list-style: none;
  }
  .contact li {
    display: flex;
    align-items: center;
    height: 29px;
    font-size: 20px;
  }
  .icon {
    width: 25px; height: 25px;
    border-radius: 50%;
    background: var(--purple);
    margin-right: 7px;
    flex: none;
    display: block;
  }
  .social {
    position: absolute;
    left: 33px;
    top: 431px;
    display: flex;
    align-items: center;
    font-size: 19px;
  }
  .social__item { display: flex; align-items: center; }
  .social__divider {
    width: 2px; height: 30px;
    background: var(--purple);
    margin: 0 9px;
  }

  /* back */
  .figure-field {
    position: absolute;
    top: 28px;
    width: 184px;
    height: 430px;
    background: var(--ghost);
    border-radius: 90px 90px 10px 10px;
  }
  .figure-field--left { left: 72px; }
  .figure-field--right { left: 650px; }
  .back-address,
  .back-url {
    position: absolute;
    left: 0; right: 0;
    text-align: center;
    color: var(--ink);
  }
  .back-address { top: 378px; font-size: 18px; }
  .back-url { top: 404px; font-size: 21px; }
</style>
</head>
<body>

<section class="card card--front" aria-label="Business card front">
  <div class="brand">
    <span class="brand__mark"></span>
    <div class="brand__name">Rosalind Vetteray<br>Gymnastics Center</div>
    <div class="brand__tagline">Gymnastics, Camps, Yoga &amp; More</div>
  </div>

  <span class="owner-tab"></span>
  <div class="owner">
    <div class="owner__name">Rosalind Vetteray</div>
    <div class="owner__title">Owner</div>
  </div>

  <ul class="contact">
    <li>
      <svg class="icon" viewBox="0 0 25 25" aria-hidden="true">
        <circle cx="12.5" cy="12.5" r="12.5" fill="#6b449b"/>
        <path d="M6 10.5c0-2 3-3 6.5-3s6.5 1 6.5 3v1h-3v-1.5h-7v1.5H6z M8 12h9l1 5H7z" fill="#fff"/>
      </svg>(216-555-0148)
    </li>
    <li>
      <svg class="icon" viewBox="0 0 25 25" aria-hidden="true">
        <circle cx="12.5" cy="12.5" r="12.5" fill="#6b449b"/>
        <rect x="6" y="8" width="13" height="9" fill="#fff"/>
        <path d="M6 8l6.5 5 6.5-5" fill="none" stroke="#6b449b" stroke-width="1.3"/>
      </svg>RosalindVetterayGymnasticsCtr@brellomail.com
    </li>
    <li>
      <svg class="icon" viewBox="0 0 25 25" aria-hidden="true">
        <circle cx="12.5" cy="12.5" r="12.5" fill="#6b449b"/>
        <g fill="none" stroke="#fff" stroke-width="1.2">
          <circle cx="12.5" cy="12.5" r="7"/>
          <ellipse cx="12.5" cy="12.5" rx="3" ry="7"/>
          <path d="M5.5 12.5h14M6.5 9h12M6.5 16h12"/>
        </g>
      </svg>www.RosalindVetterayGymnasticsCenter.example
    </li>
    <li>
      <svg class="icon" viewBox="0 0 25 25" aria-hidden="true">
        <circle cx="12.5" cy="12.5" r="12.5" fill="#6b449b"/>
        <path d="M12.5 5.5a4.8 4.8 0 0 0-4.8 4.8c0 3.6 4.8 9 4.8 9s4.8-5.4 4.8-9a4.8 4.8 0 0 0-4.8-4.8z" fill="#fff"/>
        <circle cx="12.5" cy="10.3" r="1.8" fill="#6b449b"/>
      </svg>219 W. Lantern Ridge Road, Medina, Ohio 44871
    </li>
  </ul>

  <div class="social">
    <span class="social__item"><span class="icon"></span>@VetterayGym</span>
    <span class="social__divider"></span>
    <span class="social__item"><span class="icon"></span>@VetterayGym</span>
    <span class="social__divider"></span>
    <span class="social__item"><span class="icon"></span>@RosalindVetterayGymnasticsCenter</span>
  </div>
</section>

<section class="card card--back" aria-label="Business card back">
  <div class="figure-field figure-field--left" role="img" aria-label="Faint pale lavender gymnast silhouette in a balance pose"></div>
  <div class="figure-field figure-field--right" role="img" aria-label="Faint pale lavender gymnast silhouette in a balance pose, mirrored"></div>
  <div class="brand">
    <span class="brand__mark"></span>
    <div class="brand__name">Rosalind Vetteray<br>Gymnastics Center</div>
    <div class="brand__tagline">Gymnastics, Camps, Yoga &amp; More</div>
  </div>
  <div class="back-address">219 W. Lantern Ridge Road, Medina, Ohio 44871</div>
  <div class="back-url">www.RosalindVetterayGymnasticsCenter.example</div>
</section>

</body>
</html>
```